Startup of Management Company looking for Designers!

I am looking for an upscale website. Valmoreth will focus on Real Estate, Wealth Management, and Consulting,

Target Market(s)

investors, sellers of real estate, people looking to have their real estate management.
companies looking for consulting services

Number of Pages Required

5+ page

Font styles to use
Sans Serif

Requirements
Must have
• pictures, real.

```html
<!DOCTYPE html>
<html lang="en">
<head>
<meta charset="utf-8">
<title>Valmoreth – Real Estate, Wealth Management and Consulting</title>
<link rel="stylesheet" href="https://fonts.googleapis.com/css2?family=Merriweather:wght@700;900&family=Montserrat:wght@400;500;600;700&family=Oswald:wght@600;700&display=swap">
<style>
:root{
  --navy:#0b3552;
  --navy-deep:#08283f;
  --teal:#1c6f95;
  --teal-bright:#2a93b6;
  --heading:#124e74;
  --ink:#333;
  --muted:#6b7680;
  --line:#dfe5ea;
  --white:#fff;
  --gold:#f2b01e;
}
*{box-sizing:border-box;margin:0;padding:0}
html,body{width:1200px;height:3568px;overflow:hidden}
body{font-family:"Montserrat",sans-serif;color:var(--ink);background:var(--white);position:relative}
.serif{font-family:"Merriweather",serif}
a{color:inherit;text-decoration:none}
.btn{display:inline-block;background:var(--teal-bright);color:var(--white);font-size:13px;font-weight:600;letter-spacing:.5px;padding:10px 22px;border-radius:3px;text-transform:uppercase}
.btn.small{font-size:11px;padding:8px 16px}
.btn svg{vertical-align:middle;margin-left:6px}

/* top bar */
.topbar{height:32px;background:var(--navy);display:flex;align-items:center;justify-content:space-between;padding:0 60px;color:#cfe1ec;font-size:12px}
.dots{display:flex;gap:12px}
.dot{width:12px;height:12px;border-radius:50%;background:#9fc6db}
.topbar .contact{display:flex;gap:24px;align-items:center}
.topbar .contact span{display:flex;gap:6px;align-items:center}

/* nav */
.nav{height:80px;display:flex;align-items:center;justify-content:space-between;padding:0 60px;background:var(--white)}
.brand{font-family:"Merriweather",serif;font-weight:900;font-size:24px;color:var(--heading);letter-spacing:1px}
.menu{display:flex;align-items:center;gap:26px;font-size:12px;font-weight:600;color:#445}
.menu .active{color:var(--teal-bright)}

/* hero */
.hero{position:relative;height:600px;background:linear-gradient(100deg,#1d2a33 0%,#3a4a55 35%,#7b7a72 60%,#b7ab99 100%)}
.hero-copy{position:absolute;left:60px;top:60px;width:420px;color:var(--white)}
.hero h1{font-family:"Oswald",sans-serif;font-weight:700;font-size:52px;line-height:1.08;text-transform:uppercase}
.hero h1 em{font-style:normal;color:#55b8dc}
.hero p{font-size:17px;font-weight:500;margin:20px 0 26px;line-height:1.4}
.hero-arrow{position:absolute;right:0;top:270px;width:14px;height:34px;background:var(--teal-bright)}
.scroll-down{position:absolute;left:50%;bottom:-22px;transform:translateX(-50%);width:44px;height:44px;border-radius:50%;background:var(--teal);border:3px solid var(--white);display:flex;align-items:center;justify-content:center;z-index:2}

/* welcome */
.welcome{height:428px;background:var(--teal);color:var(--white);text-align:center;padding-top:82px}
.welcome .eyebrow{font-size:13px;font-weight:500;letter-spacing:1px}
.welcome h2{font-family:"Merriweather",serif;font-size:34px;font-weight:900;margin:8px 0 24px;letter-spacing:1px}
.welcome p{width:720px;margin:0 auto 10px;font-size:13px;line-height:1.7;color:#d8ebf4}
.welcome .btn{margin-top:16px}

/* services */
.services{position:relative;height:600px;background:linear-gradient(90deg,#c9ccd0 0%,#e6e7e8 30%,#f2f3f4 60%,#e9ecef 100%)}
.services .photo{position:absolute;left:0;top:0;width:420px;height:600px;background:linear-gradient(135deg,#9aa3ab,#d9dbdc 70%,#eef0f1)}
.services .inner{position:relative;text-align:center;padding-top:80px}
.section-title{font-family:"Merriweather",serif;font-weight:900;font-size:32px;color:var(--heading);line-height:1.2;text-transform:uppercase}
.services .sub{font-size:13px;color:var(--muted);width:560px;margin:14px auto 0;line-height:1.6}
.cards{display:flex;justify-content:center;gap:32px;margin-top:38px}
.card{width:256px;height:356px;background:var(--white);box-shadow:0 4px 20px rgba(0,0,0,.12);padding:36px 24px;text-align:center}
.card .icon{height:78px;display:flex;justify-content:center;align-items:center}
.card h3{font-family:"Merriweather",serif;font-size:17px;color:var(--heading);margin:14px 0 12px}
.card p{font-size:12px;line-height:1.7;color:var(--muted);margin-bottom:22px}

/* testimonials */
.testimonials{height:560px;text-align:center;padding-top:82px}
.eyebrow-teal{font-size:12px;font-weight:600;color:var(--teal-bright);letter-spacing:1px;text-transform:uppercase}
.testimonials .section-title{margin-top:6px}
.quote-mark{margin:26px auto 22px;width:54px;height:54px;border-radius:50%;border:2px solid var(--teal);display:flex;align-items:center;justify-content:center}
.testimonials blockquote{width:620px;margin:0 auto;font-size:14px;line-height:1.8;color:var(--muted);font-style:italic}
.slider{display:flex;align-items:center;justify-content:center;gap:16px;margin-top:36px}
.slider .ctrl{font-size:11px;font-weight:600;color:var(--muted);display:flex;align-items:center;gap:6px;width:140px}
.slider .ctrl.prev{justify-content:flex-end}
.avatar{width:48px;height:48px;border-radius:50%;background:#c9d1d7}
.avatar.main{width:66px;height:66px;background:#8d8f93;border:3px solid var(--teal-bright)}
.stars{margin-top:18px;color:var(--gold);font-size:16px;letter-spacing:2px}
.client{font-family:"Merriweather",serif;font-size:14px;color:var(--teal);font-weight:700;margin-top:6px}

/* question band */
.question{position:relative;height:160px;background:linear-gradient(90deg,#1d7aa0,#0b3a5a);color:var(--white);padding:52px 0 0 140px}
.question h3{font-family:"Merriweather",serif;font-size:24px;font-weight:700}
.question .phone{display:flex;align-items:center;gap:12px;margin-top:14px;font-size:24px;font-weight:500}
.question .phone .ring{width:40px;height:40px;border-radius:50%;border:2px solid var(--white);display:flex;align-items:center;justify-content:center}
.question .pattern{position:absolute;right:60px;top:40px}

/* news */
.news{height:640px;text-align:center;padding-top:80px}
.news-grid{display:flex;justify-content:center;gap:28px;margin-top:40px}
.post{width:354px;height:440px;background:var(--white);box-shadow:0 4px 18px rgba(0,0,0,.12);text-align:left}
.post .thumb{height:180px}
.post .body{padding:22px 24px}
.post h4{font-size:16px;font-weight:700;color:#222;line-height:1.4}
.post p{font-size:12px;line-height:1.7;color:var(--muted);margin:12px 0 20px}
.post .meta{display:flex;justify-content:space-between;align-items:center;border-top:1px solid var(--line);padding-top:14px;font-size:11px;color:var(--muted)}
.post .meta span{display:flex;gap:6px;align-items:center}
.go{width:22px;height:22px;border-radius:50%;background:var(--teal);display:flex;align-items:center;justify-content:center}

/* newsletter */
.newsletter{height:160px;background:var(--navy);color:var(--white);display:flex;align-items:center;justify-content:space-between;padding:0 140px}
.newsletter h3{font-family:"Merriweather",serif;font-size:28px;font-weight:700}
.newsletter p{font-size:12px;color:#b9cfdd;margin-top:8px}
.subscribe{display:flex}
.subscribe .field{width:290px;height:40px;border:1px solid #4d7390;color:#b9cfdd;font-size:12px;padding:12px 14px}
.subscribe .btn{border-radius:0;height:40px;padding:13px 22px}

/* footer */
.footer{height:280px;background:var(--navy-deep);color:#c3d5e1;display:flex;padding:50px 140px 0;gap:60px}
.footer .about{width:300px}
.footer .brand{color:var(--white)}
.footer .about p{font-size:12px;line-height:1.7;margin:14px 0 18px}
.footer h5{font-size:13px;font-weight:700;color:var(--white);letter-spacing:1px;margin-bottom:16px;text-transform:uppercase}
.footer ul{list-style:none;font-size:12px;line-height:2}
.footer li::before{content:"› ";color:var(--teal-bright)}
.footer .contact li::before{content:""}
.footer .col{width:150px}
.footer .contact{width:220px}
.foot-dots{display:flex;gap:10px}
.foot-dots .dot{width:28px;height:28px;background:var(--teal)}
.copyright{height:28px;background:#061e30;color:#8ea8ba;font-size:11px;text-align:center;line-height:28px}
</style>
</head>
<body>

<header class="topbar">
  <div class="dots"><span class="dot"></span><span class="dot"></span><span class="dot"></span></div>
  <div class="contact">
    <span><svg width="12" height="12" viewBox="0 0 24 24" fill="#9fc6db"><path d="M6.6 10.8a15 15 0 0 0 6.6 6.6l2.2-2.2c.3-.3.7-.4 1-.2 1.1.4 2.3.6 3.6.6.6 0 1 .4 1 1V20c0 .6-.4 1-1 1A17 17 0 0 1 3 4c0-.6.4-1 1-1h3.5c.6 0 1 .4 1 1 0 1.3.2 2.5.6 3.6.1.3 0 .7-.2 1z"/></svg>123 456 7890</span>
    <span><svg width="13" height="10" viewBox="0 0 26 20" fill="none" stroke="#9fc6db" stroke-width="2"><rect x="1" y="1" width="24" height="18"/><path d="M1 1l12 10L25 1"/></svg>info@valmoreth.com</span>
  </div>
</header>

<nav class="nav">
  <div class="brand">VALMORETH</div>
  <div class="menu">
    <a class="active">HOME</a><a>ABOUT US</a><a>SERVICES</a><a>NEWS</a><a>CONTACT US</a>
    <a class="btn small">Get a Quote</a>
  </div>
</nav>

<section class="hero" role="img" aria-label="Couple reviewing financial papers at a laptop in a bright home">
  <div class="hero-copy">
    <h1>We don't tell<br>you to trust us<br><em>we earn it</em></h1>
    <p>Specialize in Real Estate, Wealth Management and Consulting</p>
    <a class="btn">Contact Us</a>
  </div>
  <div class="hero-arrow"></div>
  <div class="scroll-down"><svg width="14" height="16" viewBox="0 0 14 16" fill="none" stroke="#fff" stroke-width="2"><path d="M7 1v13M2 9l5 5 5-5"/></svg></div>
</section>

<section class="welcome">
  <div class="eyebrow">WELCOME TO</div>
  <h2>VALMORETH</h2>
  <p>Lorem Ipsum is simply dummy text of the printing and typesetting industry. Lorem Ipsum has been the industry standard dummy text ever since the 1500s when an unknown printer took a galley of type and scrambled it to make a type specimen book.</p>
  <p>It has survived not only five centuries, but also the leap into electronic typesetting, remaining essentially unchanged.</p>
  <a class="btn">Learn More <svg width="12" height="10" viewBox="0 0 12 10" fill="none" stroke="#fff" stroke-width="2"><path d="M0 5h10M6 1l4 4-4 4"/></svg></a>
</section>

<section class="services">
  <div class="photo" role="img" aria-label="Man working on a laptop in a light office"></div>
  <div class="inner">
    <h2 class="section-title">Services We<br>Provide</h2>
    <p class="sub">It has survived not only five centuries. But also the leap into electronic typesetting, remaining essentially unchanged.</p>
    <div class="cards">
      <article class="card">
        <div class="icon"><svg width="70" height="70" viewBox="0 0 70 70"><circle cx="35" cy="35" r="34" fill="#e6f1f6"/><path d="M15 36L35 18l20 18" fill="none" stroke="#124e74" stroke-width="4"/><rect x="22" y="34" width="26" height="20" fill="#1c6f95"/><rect x="31" y="42" width="8" height="12" fill="#fff"/></svg></div>
        <h3>Real Estate</h3>
        <p>Lorem Ipsum is simply dummy text of the printing and typesetting industry. Been the industry if has survived only five centuries.</p>
        <a class="btn small">Learn More <svg width="10" height="8" viewBox="0 0 12 10" fill="none" stroke="#fff" stroke-width="2"><path d="M0 5h10M6 1l4 4-4 4"/></svg></a>
      </article>
      <article class="card">
        <div class="icon"><svg width="70" height="70" viewBox="0 0 70 70"><circle cx="35" cy="35" r="34" fill="#e6f1f6"/><rect x="16" y="26" width="38" height="24" rx="3" fill="#124e74"/><circle cx="35" cy="38" r="7" fill="#fff"/><rect x="24" y="18" width="22" height="6" rx="2" fill="#1c6f95"/></svg></div>
        <h3>Wealth Management</h3>
        <p>Lorem Ipsum is simply dummy text of the printing and typesetting industry. Been the industry if has survived only five centuries.</p>
        <a class="btn small">Learn More <svg width="10" height="8" viewBox="0 0 12 10" fill="none" stroke="#fff" stroke-width="2"><path d="M0 5h10M6 1l4 4-4 4"/></svg></a>
      </article>
      <article class="card">
        <div class="icon"><svg width="70" height="70" viewBox="0 0 70 70"><circle cx="35" cy="35" r="34" fill="#e6f1f6"/><circle cx="28" cy="30" r="10" fill="none" stroke="#124e74" stroke-width="5" stroke-dasharray="4 3"/><circle cx="44" cy="44" r="8" fill="none" stroke="#1c6f95" stroke-width="5" stroke-dasharray="3 3"/></svg></div>
        <h3>Consulting</h3>
        <p>Lorem Ipsum is simply dummy text of the printing and typesetting industry. Been the industry if has survived only five centuries.</p>
        <a class="btn small">Learn More <svg width="10" height="8" viewBox="0 0 12 10" fill="none" stroke="#fff" stroke-width="2"><path d="M0 5h10M6 1l4 4-4 4"/></svg></a>
      </article>
    </div>
  </div>
</section>

<section class="testimonials">
  <div class="eyebrow-teal">Testimonials</div>
  <h2 class="section-title">What Our Client Say</h2>
  <div class="quote-mark"><svg width="22" height="18" viewBox="0 0 22 18" fill="#1c6f95"><path d="M0 18V9C0 4 3 1 8 0v3C5 4 4 6 4 8h5v10zm13 0V9c0-5 3-8 8-9v3c-3 1-4 3-4 5h5v10z"/></svg></div>
  <blockquote>Lorem Ipsum is simply dummy text of the printing and typesetting industry. Lorem Ipsum has been the industry standard dummy text ever since the 1500s, when an unknown printer took a galley of type &amp; scrambled it to make a type specimen.</blockquote>
  <div class="slider">
    <span class="ctrl prev"><svg width="14" height="8" viewBox="0 0 14 8" fill="none" stroke="#6b7680" stroke-width="1.5"><path d="M14 4H1M4 1L1 4l3 3"/></svg>PREVIOUS</span>
    <span class="avatar" role="img" aria-label="Client portrait"></span>
    <span class="avatar" role="img" aria-label="Client portrait"></span>
    <span class="avatar main" role="img" aria-label="Featured client portrait"></span>
    <span class="avatar" role="img" aria-label="Client portrait"></span>
    <span class="avatar" role="img" aria-label="Client portrait"></span>
    <span class="ctrl">NEXT<svg width="14" height="8" viewBox="0 0 14 8" fill="none" stroke="#6b7680" stroke-width="1.5"><path d="M0 4h13M10 1l3 3-3 3"/></svg></span>
  </div>
  <div class="stars">★★★★★</div>
  <div class="client">Client Name</div>
</section>

<section class="question">
  <h3>If you have An Any Question ?</h3>
  <div class="phone"><span class="ring"><svg width="18" height="18" viewBox="0 0 24 24" fill="#fff"><path d="M6.6 10.8a15 15 0 0 0 6.6 6.6l2.2-2.2c.3-.3.7-.4 1-.2 1.1.4 2.3.6 3.6.6.6 0 1 .4 1 1V20c0 .6-.4 1-1 1A17 17 0 0 1 3 4c0-.6.4-1 1-1h3.5c.6 0 1 .4 1 1 0 1.3.2 2.5.6 3.6.1.3 0 .7-.2 1z"/></svg></span>123 456 7890</div>
  <svg class="pattern" width="420" height="80" viewBox="0 0 420 80">
    <defs><pattern id="dotgrid" width="10" height="10" patternUnits="userSpaceOnUse"><circle cx="2" cy="2" r="1.2" fill="rgba(255,255,255,.25)"/></pattern></defs>
    <rect width="420" height="80" fill="url(#dotgrid)"/>
  </svg>
</section>

<section class="news">
  <h2 class="section-title">News &amp; Update</h2>
  <div class="news-grid">
    <article class="post">
      <div class="thumb" role="img" aria-label="Hands holding a small model house" style="background:linear-gradient(135deg,#1f3a52,#6d6a63 60%,#c2a57a)"></div>
      <div class="body">
        <h4>Lorem Ipsum is simply dummy text of the printing &amp; type.</h4>
        <p>Lorem Ipsum is simply dummy text of the printing and typesetting industry. Lorem Ipsum has been the industry ever since the unknown printer.</p>
        <div class="meta"><span><svg width="12" height="12" viewBox="0 0 12 12" fill="none" stroke="#1c6f95"><rect x=".5" y="1.5" width="11" height="10"/><path d="M.5 4.5h11"/></svg>20 Feb 2021</span><span class="go"><svg width="10" height="8" viewBox="0 0 12 10" fill="none" stroke="#fff" stroke-width="2"><path d="M0 5h10M6 1l4 4-4 4"/></svg></span></div>
      </div>
    </article>
    <article class="post">
      <div class="thumb" role="img" aria-label="Business people in suits shaking hands" style="background:linear-gradient(135deg,#24394e,#8ba0b2 55%,#e3e7ea)"></div>
      <div class="body">
        <h4>Lorem Ipsum is simply dummy text of the printing &amp; type.</h4>
        <p>Lorem Ipsum is simply dummy text of the printing and typesetting industry. Lorem Ipsum has been the industry ever since the unknown printer.</p>
        <div class="meta"><span><svg width="12" height="12" viewBox="0 0 12 12" fill="none" stroke="#1c6f95"><rect x=".5" y="1.5" width="11" height="10"/><path d="M.5 4.5h11"/></svg>20 February 2021</span><span class="go"><svg width="10" height="8" viewBox="0 0 12 10" fill="none" stroke="#fff" stroke-width="2"><path d="M0 5h10M6 1l4 4-4 4"/></svg></span></div>
      </div>
    </article>
    <article class="post">
      <div class="thumb" role="img" aria-label="Hourglass beside stacked coins" style="background:linear-gradient(135deg,#0f2434,#3a4c5a 55%,#b08b5a)"></div>
      <div class="body">
        <h4>Lorem Ipsum is simply dummy text of the printing &amp; type.</h4>
        <p>Lorem Ipsum is simply dummy text of the printing and typesetting industry. Lorem Ipsum has been the industry ever since the unknown printer.</p>
        <div class="meta"><span><svg width="12" height="12" viewBox="0 0 12 12" fill="none" stroke="#1c6f95"><rect x=".5" y="1.5" width="11" height="10"/><path d="M.5 4.5h11"/></svg>20 February 2021</span><span class="go"><svg width="10" height="8" viewBox="0 0 12 10" fill="none" stroke="#fff" stroke-width="2"><path d="M0 5h10M6 1l4 4-4 4"/></svg></span></div>
      </div>
    </article>
  </div>
</section>

<section class="newsletter">
  <div>
    <h3>Subscribe to Our Newsletters</h3>
    <p>Would you like to receive our exclusive updates for signing our newsletter ?</p>
  </div>
  <div class="subscribe"><div class="field">Enter Email *</div><a class="btn">Subscribe</a></div>
</section>

<footer class="footer">
  <div class="about">
    <div class="brand">VALMORETH</div>
    <p>Lorem Ipsum is simply dummy text of the printing and typesetting industry. Lorem Ipsum has been the industry standard text ever since the unknown printer.</p>
    <div class="foot-dots"><span class="dot"></span><span class="dot"></span><span class="dot"></span></div>
  </div>
  <div class="col">
    <h5>Sitemap</h5>
    <ul><li>Home</li><li>About</li><li>Services</li><li>News</li><li>Contact Us</li></ul>
  </div>
  <div class="col">
    <h5>Services</h5>
    <ul><li>Real Estate</li><li>Wealth Management</li><li>Consulting</li></ul>
  </div>
  <div class="contact">
    <h5>Contact Us</h5>
    <ul><li>Valmoreth</li><li>301 - Lorem ipsum street, your city state zip</li><li>123 456 7890</li><li>info@valmoreth.com</li></ul>
  </div>
</footer>
<div class="copyright">©Valmoreth - 2021 All rights reserved.</div>

</body>
</html>
```